Makeup artist looking for business card design

- Business card to be memorable and recognisable

- I've attached photos of my logo (File 4), photos that I want to incorporate into the design (File 5,6 & 7) and an example of the design I like "Mirela Stott" (File 1)

- I've attached 3 photos of the designs I want to use, please use one of your choice

- Next to Instagram (File 2) and Facebook (File 3), please use their logo.

- No coloured background, either use the original background (grey) old white.

- Please include the following on the business card:
- Business name: LK Makeup Artistry
- My name: Rosalind Kerr
- Occupation: Makeup Artist
- Contact number: 0437 295 148
- Email: roskerr_makeup@mailvento.com
- Instagram (please use image): @lkmakeupartistry
- Facebook (please use image): www.facebook.com/LKMakeUpArtistry

Target Market(s)

Target woman for bridal makeup, occasion, fashion makeup and print.

Industry/Entity Type

Business

Requirements
Must have
• Logo provided and photo provided
Should not have
• Colourful background
Too cluttered
Shouldn't use old style font

```html
<!DOCTYPE html>
<html lang="en">
<head>
<meta charset="utf-8">
<title>Rosalind Kerr – Business Card</title>
<link href="https://fonts.googleapis.com/css2?family=Raleway:wght@200;300;400&family=Lato:wght@400&display=swap" rel="stylesheet">
<style>
  :root {
    --backdrop: #ecebea;
    --lilac: #c99dcc;
    --lilac-deep: #b583b9;
    --lilac-text: #b58bc7;
    --ink: #0c1514;
    --ink-soft: #1a2423;
    --logo-ink: #2b2430;
    --contact-text: #e6dfe8;
    --icon-fill: #8f7599;
    --photo-light: #f1d7dc;
    --photo-mid: #d6a9cf;
    --photo-shade: #9c7fa8;
  }
  * { box-sizing: border-box; margin: 0; padding: 0; }
  html, body {
    width: 1200px;
    height: 800px;
    overflow: hidden;
  }
  body {
    background: var(--backdrop);
    position: relative;
    font-family: "Lato", sans-serif;
  }

  /* Back of card */
  .card-back {
    position: absolute;
    left: 120px;
    top: 130px;
    width: 340px;
    height: 540px;
    background: linear-gradient(180deg, var(--lilac) 0%, var(--lilac-deep) 100%);
    display: flex;
    align-items: center;
    justify-content: center;
    box-shadow: 0 10px 28px rgba(0,0,0,0.18);
  }
  .brand-mark {
    display: flex;
    align-items: center;
    gap: 12px;
    font-family: "Raleway", sans-serif;
    font-weight: 300;
    font-size: 17px;
    letter-spacing: 3px;
    text-transform: uppercase;
    color: var(--logo-ink);
  }
  .brand-dot {
    width: 10px;
    height: 10px;
    border-radius: 50%;
    background: var(--logo-ink);
  }

  /* Front of card */
  .card-front {
    position: absolute;
    left: 520px;
    top: 225px;
    width: 600px;
    height: 350px;
    background: linear-gradient(180deg, var(--ink-soft) 0%, var(--ink) 45%, #000 100%);
    overflow: hidden;
    box-shadow: 0 10px 28px rgba(0,0,0,0.25);
  }
  .identity {
    position: absolute;
    left: 34px;
    top: 26px;
  }
  .person-name {
    font-family: "Raleway", sans-serif;
    font-weight: 300;
    font-size: 34px;
    letter-spacing: 4px;
    text-transform: uppercase;
    color: var(--lilac-text);
  }
  .occupation {
    font-family: "Lato", sans-serif;
    font-size: 13px;
    color: var(--lilac-text);
    margin-top: 2px;
  }
  .contact-list {
    list-style: none;
    margin-top: 14px;
  }
  .contact-item {
    display: flex;
    align-items: center;
    gap: 10px;
    font-size: 13px;
    color: var(--contact-text);
    line-height: 22px;
  }
  .contact-icon {
    width: 14px;
    height: 14px;
    flex: none;
  }
  .contact-square {
    width: 14px;
    height: 14px;
    flex: none;
    border-radius: 2px;
    background: var(--icon-fill);
  }
  .portrait-area {
    position: absolute;
    left: 230px;
    top: 160px;
    width: 370px;
    height: 190px;
    background: linear-gradient(110deg, var(--photo-light) 0%, var(--photo-mid) 55%, var(--photo-shade) 100%);
  }
</style>
</head>
<body>
  <section class="card-back">
    <div class="brand-mark">
      <span class="brand-dot"></span>
      <span class="brand-name">LK Makeup Artistry</span>
    </div>
  </section>

  <section class="card-front">
    <div class="identity">
      <h1 class="person-name">Rosalind Kerr</h1>
      <p class="occupation">Makeup Artist</p>
      <ul class="contact-list">
        <li class="contact-item">
          <svg class="contact-icon" viewBox="0 0 14 14" aria-hidden="true">
            <rect width="14" height="14" rx="2" fill="var(--icon-fill)"/>
            <rect x="4.5" y="2.5" width="5" height="9" rx="1" fill="none" stroke="var(--ink)" stroke-width="1.2"/>
          </svg>
          <span>0437 295 148</span>
        </li>
        <li class="contact-item">
          <svg class="contact-icon" viewBox="0 0 14 14" aria-hidden="true">
            <rect width="14" height="14" rx="2" fill="var(--icon-fill)"/>
            <rect x="2.5" y="4" width="9" height="6.5" fill="none" stroke="var(--ink)" stroke-width="1.1"/>
            <polyline points="2.5,4 7,8 11.5,4" fill="none" stroke="var(--ink)" stroke-width="1.1"/>
          </svg>
          <span>roskerr_makeup@mailvento.com</span>
        </li>
        <li class="contact-item">
          <span class="contact-square"></span>
          <span>@lkmakeupartistry</span>
        </li>
        <li class="contact-item">
          <span class="contact-square"></span>
          <span>/LKMakeUpArtistry</span>
        </li>
      </ul>
    </div>
    <div class="portrait-area" role="img" aria-label="Beauty portrait of a model with lilac lipstick framed by pale pink petals"></div>
  </section>
</body>
</html>
```